Brintell's Business Card

I need some designs for a new business card including the new logo attached. An old example of our business card is also attached to show all the data that should be included on the new design.
**I added some more examples someone had mocked up**

Contact Information for Business Card

Should include all info on other examples uploaded.

```html
<!DOCTYPE html>
<html lang="en">
<head>
<meta charset="utf-8">
<title>Brintell's Business Card</title>
<link href="https://fonts.googleapis.com/css2?family=Open+Sans:wght@400;600;700&display=swap" rel="stylesheet">
<style>
  :root {
    --backdrop: #202020;
    --card-white: #ffffff;
    --brand-red: #ec1c24;
    --brand-blue: #1066b5;
    --ink: #3a3a3a;
    --on-red: #ffffff;
  }
  * { margin: 0; padding: 0; box-sizing: border-box; }
  html, body { width: 1047px; height: 1200px; overflow: hidden; }
  body {
    background: var(--backdrop);
    font-family: "Open Sans", sans-serif;
    position: relative;
  }
  .card {
    position: absolute;
    left: 156px;
    width: 743px;
    height: 424px;
    border-radius: 18px;
    overflow: hidden;
  }
  .card-front { top: 120px; background: var(--card-white); }
  .card-back { top: 634px; background: var(--brand-red); color: var(--on-red); }

  .brand-lockup {
    position: absolute;
    display: flex;
    align-items: center;
  }
  .brand-dot { border-radius: 50%; flex: none; }
  .brand-name { font-weight: 700; line-height: 1; white-space: nowrap; }

  .card-front .brand-lockup { right: 44px; top: 66px; gap: 14px; }
  .card-front .brand-dot { width: 46px; height: 46px; background: var(--brand-red); }
  .card-front .brand-name { font-size: 46px; color: var(--brand-blue); }

  .holder-name {
    position: absolute;
    left: 46px; top: 232px;
    font-size: 32px; font-weight: 700;
    color: var(--brand-blue);
    letter-spacing: 0.2px;
  }
  .name-rule {
    position: absolute;
    left: 46px; top: 280px;
    width: 654px; height: 3px;
    background: var(--brand-red);
  }
  .contact-list { position: absolute; left: 46px; top: 300px; list-style: none; }
  .contact-item {
    display: flex; align-items: center; gap: 10px;
    color: var(--ink); height: 29px;
  }
  .contact-item svg { width: 18px; height: 18px; flex: none; fill: var(--brand-blue); }
  .contact-phone { font-size: 21px; }
  .contact-email { font-size: 18px; }

  .front-band { position: absolute; left: 0; bottom: 0; width: 743px; height: 40px; }
  .front-band svg { position: absolute; inset: 0; }
  .band-text {
    position: absolute; top: 0; line-height: 40px;
    font-size: 20px; font-weight: 600; color: var(--on-red);
  }
  .band-left { left: 78px; }
  .band-right { right: 36px; }

  .card-back .brand-lockup { left: 85px; top: 128px; gap: 22px; }
  .card-back .brand-dot { width: 118px; height: 118px; background: var(--on-red); }
  .card-back .brand-name { font-size: 74px; }

  .service-area {
    position: absolute; left: 0; right: 0; top: 332px;
    text-align: center; font-size: 22px; font-weight: 700; letter-spacing: 0.4px;
  }
  .back-rule {
    position: absolute; left: 51px; top: 363px;
    width: 641px; height: 2px; background: var(--on-red);
  }
  .call-to-action {
    position: absolute; left: 0; right: 0; top: 370px;
    text-align: center; font-size: 17px; font-weight: 600;
  }
</style>
</head>
<body>
  <section class="card card-front">
    <div class="brand-lockup">
      <span class="brand-dot"></span>
      <span class="brand-name">BRINTELL'S</span>
    </div>

    <h1 class="holder-name">MARK BRINTELL</h1>
    <div class="name-rule"></div>

    <ul class="contact-list">
      <li class="contact-item contact-phone">
        <svg viewBox="0 0 24 24" aria-hidden="true"><path d="M6.6 10.8a15.1 15.1 0 0 0 6.6 6.6l2.2-2.2a1 1 0 0 1 1-.25 11.4 11.4 0 0 0 3.6.57 1 1 0 0 1 1 1V20a1 1 0 0 1-1 1A17 17 0 0 1 3 4a1 1 0 0 1 1-1h3.5a1 1 0 0 1 1 1c0 1.25.2 2.45.57 3.57a1 1 0 0 1-.25 1z"/></svg>
        <span>555.014.2290</span>
      </li>
      <li class="contact-item contact-email">
        <svg viewBox="0 0 24 24" aria-hidden="true"><path d="M2 5h20v14H2z M4 7v.4l8 5.2 8-5.2V7z" fill-rule="evenodd"/></svg>
        <span>hvacbrintell@mailbox.com</span>
      </li>
    </ul>

    <div class="front-band">
      <svg viewBox="0 0 743 40" preserveAspectRatio="none" aria-hidden="true">
        <rect width="743" height="40" fill="var(--brand-red)"/>
        <path d="M0 0 H345 C375 0 385 38 420 40 H0 Z" fill="var(--brand-blue)"/>
        <path d="M345 0 C375 0 385 38 420 40 H412 C380 36 370 2 345 2 Z" fill="var(--card-white)"/>
      </svg>
      <span class="band-text band-left">LICENSED &amp; INSURED</span>
      <span class="band-text band-right">FAMILY OWNED &amp; OPERATED</span>
    </div>
  </section>

  <section class="card card-back">
    <div class="brand-lockup">
      <span class="brand-dot"></span>
      <span class="brand-name">BRINTELL'S</span>
    </div>
    <p class="service-area">SERVES MILLBROOK, IA &amp; SURROUNDING AREAS</p>
    <div class="back-rule"></div>
    <p class="call-to-action">CALL TODAY FOR ALL YOUR HVAC, REFRIGERATION &amp; PLUMBING NEEDS</p>
  </section>
</body>
</html>
```